Bookkeeping Book Design

I need a book design for my new book. I would like someone who will design the front, back, and spine. It will have an ISBN # and I am sending my picture to be placed at the back. I provide bookkeeping services to many industries such as real estate, construction, cleaning, etc. Since I am dealing with people's money, I am looking for the colors blue, green and white. The design should communicate organization, management of time and money efficiently and trust.
Title: Ledger Harbor Methods
Subtitle: A Complete Handbook for Orderly Accounts
Author: Odile Braskovich
Construction

```html
<!DOCTYPE html>
<html lang="en">
<head>
<meta charset="utf-8">
<title>Ledger Harbor Methods – Book Cover</title>
<link rel="stylesheet" href="https://fonts.googleapis.com/css2?family=Cinzel:wght@500;600&family=Arimo:wght@400&display=swap">
<style>
  :root {
    --stage: #000000;
    --navy: #263f73;
    --blue-mid: #2a78c2;
    --cyan: #1ea8e6;
    --cyan-light: #4dbdee;
    --silver-light: #f4f5f7;
    --silver: #d3d8dd;
    --silver-dark: #8d969f;
    --rim-dark: #5d666f;
    --band: #1d3159;
    --white: #ffffff;
  }
  html, body {
    margin: 0;
    padding: 0;
    width: 1200px;
    height: 1200px;
    overflow: hidden;
    background: var(--stage);
  }
  .canvas {
    position: relative;
    width: 1200px;
    height: 1200px;
    background: var(--stage);
  }
  .book-cover {
    position: absolute;
    left: 300px;
    top: 120px;
    width: 600px;
    height: 960px;
    overflow: hidden;
    background: linear-gradient(180deg, var(--navy) 0%, var(--blue-mid) 32%, var(--cyan) 60%, var(--cyan-light) 100%);
    box-shadow: 0 0 0 1px #0d1a33;
  }
  .title {
    position: absolute;
    top: 36px;
    left: 0;
    width: 100%;
    margin: 0;
    text-align: center;
    font-family: "Cinzel", serif;
    font-weight: 500;
    color: var(--white);
    line-height: 1;
  }
  .title-line {
    display: block;
    font-size: 106px;
    letter-spacing: 1px;
    margin-bottom: 4px;
    white-space: nowrap;
  }
  .title-line--first {
    font-size: 100px;
  }
  .title-dash {
    display: inline-block;
    width: 44px;
    height: 6px;
    background: var(--white);
    vertical-align: middle;
    margin: 0 12px 14px;
  }
  .subtitle {
    position: absolute;
    top: 366px;
    left: 0;
    width: 100%;
    margin: 0;
    text-align: center;
    font-family: "Arimo", sans-serif;
    font-size: 26px;
    color: var(--white);
  }
  .cover-artwork {
    position: absolute;
    left: 0;
    top: 500px;
    width: 600px;
    height: 402px;
  }
  .author-band {
    position: absolute;
    left: 0;
    bottom: 0;
    width: 100%;
    height: 58px;
    background: linear-gradient(180deg, #2b4680 0%, var(--band) 100%);
    display: flex;
    align-items: center;
    justify-content: center;
  }
  .author-name {
    margin: 0;
    font-family: "Cinzel", serif;
    font-weight: 500;
    font-size: 31px;
    letter-spacing: 2px;
    color: var(--white);
  }
</style>
</head>
<body>
<main class="canvas">
  <section class="book-cover">
    <h1 class="title">
      <span class="title-line title-line--first"><span class="title-dash"></span>Ledger<span class="title-dash"></span></span>
      <span class="title-line">Harbor</span>
      <span class="title-line">Methods</span>
    </h1>
    <p class="subtitle">A Complete Handbook for Orderly Accounts</p>

    <svg class="cover-artwork" viewBox="0 0 600 402" role="img" aria-label="Chrome efficiency gauge with a red needle pointing near ninety percent">
      <defs>
        <linearGradient id="rimTone" x1="0" y1="0" x2="1" y2="1">
          <stop offset="0" stop-color="#eef0f2"/>
          <stop offset="0.5" stop-color="#a3abb3"/>
          <stop offset="1" stop-color="#5d666f"/>
        </linearGradient>
        <radialGradient id="faceTone" cx="0.4" cy="0.55" r="0.6">
          <stop offset="0" stop-color="#ffffff"/>
          <stop offset="0.7" stop-color="#e6e9ec"/>
          <stop offset="1" stop-color="#c4cad0"/>
        </radialGradient>
      </defs>
      <circle class="gauge-rim" cx="170" cy="370" r="356" fill="url(#rimTone)"/>
      <circle class="gauge-face" cx="170" cy="370" r="318" fill="url(#faceTone)"/>
    </svg>

    <footer class="author-band">
      <p class="author-name">Odile Braskovich</p>
    </footer>
  </section>
</main>
</body>
</html>
```